silverbrook gymnastics academy

need a website for above to contain information about the academy, enrollment form etc..

Need a web design for new business Silverbrook Gymnastics Academy offering classes in gymnastics. Info on the business is in the doc called "Web design" which details the tabs I will need on my page. Please see our Facebook page to get an idea of the style Silverbrookgymnasticsacademy.

Thank you for your help. I do not require hosting of a domain name just need it all ready to be hosted. Thanks

Budget now increased to include the coding of the website as well.

```html
<!DOCTYPE html>
<html lang="en">
<head>
<meta charset="utf-8">
<title>Silverbrook Gymnastics Academy</title>
<link rel="stylesheet" href="https://fonts.googleapis.com/css2?family=Raleway:wght@400;500;700;800&family=Open+Sans:wght@400;600;700&family=Arimo:wght@400;700&display=swap">
<style>
  :root {
    --gold: #e0ae2a;
    --ink: #1d1d1d;
    --white: #ffffff;
    --mist: #f1f1f1;
    --card: #000000;
    --footer: #9b9b9b;
    --line: #bdbdbd;
  }
  * { box-sizing: border-box; margin: 0; padding: 0; }
  html, body { width: 790px; height: 1200px; overflow: hidden; }
  body { position: relative; background: var(--white); font-family: "Arimo", Arial, sans-serif; color: var(--ink); }

  .top-rule { position: absolute; left: 0; top: 0; width: 790px; height: 3px; background: var(--gold); }

  .site-header { position: absolute; left: 0; top: 3px; width: 790px; height: 83px; background: var(--white); box-shadow: 0 1px 3px rgba(0,0,0,.35); z-index: 2; }
  .brand { position: absolute; left: 66px; top: 16px; font-family: "Raleway", sans-serif; font-weight: 500; color: var(--ink); line-height: 1; }
  .brand-line1 { font-size: 21px; letter-spacing: .3px; }
  .brand-line2 { font-size: 17px; margin-top: 12px; letter-spacing: .3px; }

  .social-top { position: absolute; left: 600px; top: 11px; display: flex; gap: 5px; }
  .social-top span { width: 16px; height: 16px; border-radius: 50%; background: var(--ink); display: block; }

  .main-nav { position: absolute; top: 41px; left: 404px; display: flex; align-items: center; font-family: "Raleway", sans-serif; font-size: 11px; font-weight: 500; }
  .main-nav a { color: var(--ink); text-decoration: none; }
  .main-nav .nav-home { background: var(--gold); color: var(--white); padding: 6px 10px; border-radius: 3px; font-weight: 700; margin-right: 35px; }
  .main-nav .nav-about { margin-right: 44px; }
  .main-nav .nav-contact { margin-right: 44px; }

  .hero { position: absolute; left: 0; top: 86px; width: 790px; height: 351px;
    background: linear-gradient(180deg, #5f6a7c 0%, #4e5566 40%, #7a5d4d 70%, #5c4436 100%); }
  .hero-caption { position: absolute; left: 66px; top: 217px; width: 342px; height: 117px; background: rgba(40,32,28,.35); border: 1px solid rgba(255,255,255,.18); padding: 8px 12px; }
  .hero-caption h1 { font-family: "Raleway", sans-serif; font-weight: 800; font-size: 31px; color: var(--gold); line-height: 1.1; }
  .hero-caption p { margin-top: 8px; width: 300px; font-family: "Raleway", sans-serif; font-size: 12.5px; line-height: 16px; color: var(--white); }

  .welcome { position: absolute; left: 0; top: 437px; width: 790px; height: 176px; background: var(--mist); text-align: center; }
  .welcome h2 { margin-top: 33px; font-family: "Open Sans", sans-serif; font-weight: 600; font-size: 19px; color: var(--gold); }
  .welcome p { width: 645px; margin: 10px auto 0; font-size: 9.6px; line-height: 16px; color: #222; }
  .welcome p + p { margin-top: 16px; }

  .programs { position: absolute; left: 0; top: 658px; width: 790px; height: 167px; }
  .program { position: absolute; top: 0; width: 203px; height: 167px; background: var(--card); color: var(--white); text-align: center; font-family: "Arimo", sans-serif; }
  .program .photo { width: 100%; display: block; }
  .program-clinics { left: 75px; }
  .program-camps { left: 290px; }
  .program-solutions { left: 512px; }
  .program-clinics .photo, .program-solutions .photo { height: 122px; }
  .program-clinics .photo { background: linear-gradient(180deg, #8a7ea2 0%, #4d6fa0 60%, #3a6aa8 100%); }
  .program-solutions .photo { background: linear-gradient(180deg, #c9cfd6 0%, #8a98b0 55%, #2f5fb8 100%); }
  .program-camps .photo { height: 76px; background: linear-gradient(180deg, #6b4f96 0%, #5c3c8a 100%); }
  .program h3 { font-weight: 400; font-size: 19px; line-height: 45px; }
  .program-camps .plus { position: absolute; left: 81px; top: 56px; width: 40px; height: 40px; border-radius: 50%; background: var(--gold); border: 3px solid #111; }
  .program-camps h3 { margin-top: 26px; line-height: 1; }
  .program-camps p { margin: 10px 16px 0; font-size: 7px; line-height: 12px; color: var(--white); }

  .contact { position: absolute; left: 0; top: 865px; width: 790px; height: 242px;
    background: linear-gradient(160deg, #3a3540 0%, #2a2c33 45%, #1e3438 100%); color: var(--white); }
  .contact h2 { position: absolute; left: 282px; top: 14px; width: 226px; text-align: center; font-family: "Open Sans", sans-serif; font-weight: 700; font-size: 30px; letter-spacing: 1px; padding-bottom: 2px; border-bottom: 2px solid #8a8a8a; }
  .contact-info { position: absolute; left: 66px; top: 80px; width: 302px; height: 111px; border: 1px solid var(--white); padding: 7px 10px; }
  .contact-info h3 { font-family: "Raleway", sans-serif; font-weight: 500; font-size: 17px; letter-spacing: .5px; }
  .info-row { display: flex; align-items: center; gap: 9px; font-size: 12px; margin-top: 14px; }
  .info-row + .info-row { margin-top: 14px; }
  .contact-form .field { position: absolute; border: 1px solid var(--white); font-family: "Arimo", sans-serif; font-weight: 700; font-size: 9px; padding: 5px 5px; }
  .field-name { left: 423px; top: 80px; width: 145px; height: 23px; }
  .field-email { left: 580px; top: 80px; width: 145px; height: 23px; }
  .field-message { left: 423px; top: 119px; width: 302px; height: 72px; }

  .site-footer { position: absolute; left: 0; top: 1107px; width: 790px; height: 72px; background: var(--footer); color: var(--white); text-align: center; }
  .footer-nav { margin-top: 17px; font-size: 11px; font-family: "Raleway", sans-serif; font-weight: 500; display: flex; justify-content: center; gap: 27px; }
  .social-bottom { display: flex; justify-content: center; gap: 19px; margin-top: 14px; }
  .social-bottom span { width: 13px; height: 13px; border-radius: 50%; background: var(--white); display: block; }
  .copyright { position: absolute; left: 0; top: 1179px; width: 790px; height: 21px; background: var(--gold); font-size: 8px; line-height: 21px; text-align: center; color: #222; }
</style>
</head>
<body>
  <div class="top-rule"></div>

  <header class="site-header">
    <div class="brand">
      <div class="brand-line1">SILVERBROOK GYMNASTICS</div>
      <div class="brand-line2">ACADEMY &nbsp;SGA</div>
    </div>
    <div class="social-top" aria-label="Social links"><span></span><span></span><span></span><span></span><span></span><span></span></div>
    <nav class="main-nav">
      <a class="nav-home" href="#">Home</a>
      <a class="nav-about" href="#">About us</a>
      <a class="nav-contact" href="#">Contact Us</a>
      <a href="#">More info</a>
    </nav>
  </header>

  <section class="hero" role="img" aria-label="Gymnast in a blue leotard leaping mid-routine in front of a crowded arena">
    <div class="hero-caption">
      <h1>Lorem ipsum dolor</h1>
      <p>Sed interdum, lacus et vulputate pellentesque, velit nulla &nbsp;ipsum dolor sit amet communitas facilisi congue eu ornare vel, mattis sed eros.</p>
    </div>
  </section>

  <section class="welcome">
    <h2>WELCOME TO SILVERBROOK GYMNASTICS ACADEMY</h2>
    <p>simply dummy text of the printing and typesetting industry. Lorem Ipsum has been the industry's standard dummy text ever since the 1500s, when an unknown printer took a galley of type and scrambled it to make a type specimen book. It has survived not only five centuries,</p>
    <p>but also the leap into electronic typesetting, remaining essentially unchanged release of Lindale sheets containing Lorem Ipsum passages, and more recently with desktop publishing software like Quillpage Studio including versions of Lorem Ipsum.</p>
  </section>

  <section class="programs">
    <article class="program program-clinics">
      <div class="photo" role="img" aria-label="Coach leading a group of gymnasts stretching on a blue floor mat"></div>
      <h3>Coaches Clinics</h3>
    </article>
    <article class="program program-camps">
      <div class="photo" role="img" aria-label="Team of athletes in purple uniforms posing in a gym"></div>
      <div class="plus"><svg width="34" height="34" viewBox="0 0 34 34"><path d="M17 9v16M9 17h16" stroke="#fff" stroke-width="3" stroke-linecap="round"/></svg></div>
      <h3>Volleyball Camps</h3>
      <p>Lorem Ipsum has been the industry's standard dummy text ever since the 1500s, when an</p>
    </article>
    <article class="program program-solutions">
      <div class="photo" role="img" aria-label="Coach helping a young gymnast with a split stretch on blue mats"></div>
      <h3>Coaches Solutions</h3>
    </article>
  </section>

  <section class="contact" role="img" aria-label="Dimmed gym scene with gymnasts in teal leotards behind the contact area">
    <h2>CONTACT US</h2>
    <div class="contact-info">
      <h3>CONTACT INFO</h3>
      <div class="info-row">
        <svg width="20" height="20" viewBox="0 0 20 20"><circle cx="10" cy="10" r="9" fill="none" stroke="#e0ae2a" stroke-width="1.6"/><path d="M7 5.5c-1 .6-1.3 2-.6 3.6.9 2 2.4 3.6 4.3 4.6 1.4.7 2.6.5 3.2-.4l-1.6-1.6-1.2.7c-1.2-.6-2-1.5-2.6-2.7l.7-1.2z" fill="#e0ae2a"/></svg>
        <span>5550143298</span>
      </div>
      <div class="info-row">
        <svg width="20" height="14" viewBox="0 0 20 14"><rect x="0.5" y="0.5" width="19" height="13" fill="#e0ae2a"/><path d="M1 1l9 7 9-7M1 13l7-6M19 13l-7-6" stroke="#7a5a10" stroke-width="1" fill="none"/></svg>
        <span>info@silverbrookgym.example</span>
      </div>
    </div>
    <form class="contact-form">
      <div class="field field-name">Full Name</div>
      <div class="field field-email">Email</div>
      <div class="field field-message">Message</div>
    </form>
  </section>

  <footer class="site-footer">
    <div class="footer-nav"><span>Home</span><span>|</span><span>About us</span><span>|</span><span>Contact Us</span></div>
    <div class="social-bottom" aria-label="Social links"><span></span><span></span><span></span><span></span><span></span><span></span></div>
  </footer>
  <div class="copyright">Copyright © 2014 All Rights Reserved | Privacy Policy</div>
</body>
</html>
```